Need a business cards for a hair dressing salon.

Target Market(s)

Target woman for Hair cuts, bridal makeup, occasion, fashion makeup and etc.

Industry/Entity Type

Hair

Font styles to use
Serif
Script

Requirements
Must have
• - Business card to be memorable and recognizable

- Please include the following on the business card:
- Business name: Salon Orimba
- Name: Kalini Desmodo (Name Must be changeable)
- Occupation: Hair Dresser & Beautician
- Contact number: 04 739 2 HAIR
- Email: mail@orimba.com.au
- Facebook (please use image): www.facebook.com/orimba.com.au
Nice to have
• Font Styles:
Business Name - Script
Other Text - Serif

```html
<!DOCTYPE html>
<html lang="en">
<head>
<meta charset="utf-8">
<title>Salon Orimba – Business Card</title>
<link rel="stylesheet" href="https://fonts.googleapis.com/css2?family=Great+Vibes&family=Cormorant+Garamond:wght@500&display=swap">
<style>
  :root {
    --page-bg: #ecebe8;
    --card-cream: #fce8d6;
    --card-cream-light: #fff5ec;
    --brand-orange: #f26522;
    --band-text: #ffffff;
  }
  * { margin: 0; padding: 0; box-sizing: border-box; }
  html, body {
    width: 1200px;
    height: 918px;
    overflow: hidden;
    background: var(--page-bg);
  }
  .canvas {
    position: relative;
    width: 1200px;
    height: 918px;
  }
  .business-card {
    position: absolute;
    left: 100px;
    top: 153px;
    width: 1000px;
    height: 611px;
    overflow: hidden;
    background: var(--card-cream);
    box-shadow: 0 6px 24px rgba(0,0,0,0.12);
  }
  .damask-field {
    position: absolute;
    inset: 0 0 111px 0;
    background: radial-gradient(ellipse at 50% 40%, var(--card-cream-light) 0%, var(--card-cream) 75%);
  }
  .brand-name {
    position: absolute;
    font-family: "Great Vibes", cursive;
    font-weight: 400;
    color: var(--brand-orange);
    line-height: 1;
    white-space: nowrap;
  }
  .brand-name--first { left: 44px; top: 110px; font-size: 150px; }
  .brand-name--second { left: 470px; top: 190px; font-size: 150px; }
  .brand-mark {
    position: absolute;
    left: 368px;
    top: 120px;
    width: 92px;
    height: 92px;
    border-radius: 50%;
    background: var(--brand-orange);
  }
  .holder-name {
    position: absolute;
    left: 300px;
    top: 318px;
    font-family: "Cormorant Garamond", serif;
    font-weight: 500;
    font-size: 46px;
    color: var(--brand-orange);
  }
  .holder-role {
    position: absolute;
    left: 300px;
    top: 376px;
    font-family: "Cormorant Garamond", serif;
    font-weight: 500;
    font-size: 26px;
    letter-spacing: 0.5px;
    text-transform: uppercase;
    color: var(--brand-orange);
  }
  .contact-band {
    position: absolute;
    left: 0;
    bottom: 0;
    width: 100%;
    height: 111px;
    background: var(--brand-orange);
    display: flex;
    align-items: center;
    justify-content: space-between;
    padding: 0 44px;
    font-family: "Cormorant Garamond", serif;
    font-weight: 500;
    font-size: 27px;
    color: var(--band-text);
  }
  .contact-item {
    display: flex;
    align-items: center;
    gap: 12px;
  }
  .contact-icon { width: 24px; height: 24px; flex: none; }
  .contact-at { font-size: 28px; line-height: 1; }
</style>
</head>
<body>
<main class="canvas">
  <section class="business-card">
    <div class="damask-field" role="img" aria-label="Soft cream damask floral pattern background"></div>

    <span class="brand-name brand-name--first">Salon</span>
    <span class="brand-mark" aria-hidden="true"></span>
    <span class="brand-name brand-name--second">Orimba</span>

    <p class="holder-name">Kalini Desmodo</p>
    <p class="holder-role">Hair Dresser &amp; Beautician</p>

    <footer class="contact-band">
      <span class="contact-item">
        <svg class="contact-icon" viewBox="0 0 24 24" aria-hidden="true">
          <path d="M6.6 3.5l2.6 2.6c.5.5.5 1.2.1 1.7L7.9 9.4c1.1 2.5 3.2 4.6 5.7 5.7l1.6-1.4c.5-.4 1.2-.4 1.7.1l2.6 2.6c.5.5.5 1.3 0 1.8l-1.5 1.5c-.8.8-2 1-3 .6C9.6 18.4 5.6 14.4 3.7 9c-.4-1-.2-2.2.6-3l1.5-1.5c.2-.4 .5-.5.8-1z" fill="none" stroke="currentColor" stroke-width="1.6" stroke-linejoin="round"/>
        </svg>
        04 739 2 HAIR
      </span>
      <span class="contact-item">
        <span class="contact-at" aria-hidden="true">@</span>
        mail@orimba.com.au
      </span>
      <span class="contact-item">
        <svg class="contact-icon" viewBox="0 0 24 24" aria-hidden="true">
          <rect x="2" y="2" width="20" height="20" fill="none" stroke="currentColor" stroke-width="1.8"/>
        </svg>
        /orimba.com.au
      </span>
    </footer>
  </section>
</main>
</body>
</html>
```